BRIGHT COLORFUL + 55 FAMILY HISTORY BROCHURE 11 x 17 bifold

11 x 17 Bifold Flyer I have given you the Layout I just need you to make it Pretty

YOU DO NOT NEED TO FOLLOW MY LAYOUT, You can but dont have too

Target Market(s)

55 year old consumers, who could choose our service of Hereditary Cancer Screening

Industry/Entity Type

Health And Wellness

Requirements
Must have
• Must be appealing to Grand Parents, must make them want to test , show lots of pictures of grand children, YOU DO NOT NEED TO FOLLOW MY LAYOUT , You can but dont have too
Nice to have
• use our colors of our logo , YOU DO NOT NEED TO FOLLOW MY LAYOUT , You can but dont have too
Should not have
• YOU DO NOT NEED TO FOLLOW MY LAYOUT, You can but dont have too

```html
<!DOCTYPE html>
<html lang="en">
<head>
<meta charset="utf-8">
<title>Hereditary Cancer Screening Bifold</title>
<link rel="stylesheet" href="https://fonts.googleapis.com/css2?family=Libre+Baskerville:wght@400;700&family=Crimson+Pro:wght@400;600&family=Russo+One&family=Montserrat:wght@600&family=Arimo&display=swap">
<style>
  :root{
    --navy:#0b0a5e;
    --glow:#3b3ab0;
    --yellow:#f4d80c;
    --lime:#c6f000;
    --white:#ffffff;
    --frame:#ffffff;
    --brand-bg:#eceef5;
    --brand-ink:#1b2a6b;
    --photo-warm:#c9a98c;
    --photo-green:#7f9a5a;
    --photo-soft:#d9c8b8;
  }
  html,body{margin:0;padding:0;overflow:hidden;background:#000;}
  .spread{position:relative;width:1200px;height:927px;overflow:hidden;background:var(--navy);font-family:"Crimson Pro",serif;}
  .panel{position:absolute;top:0;height:927px;width:600px;box-sizing:border-box;}
  .panel--inside{left:0;background:radial-gradient(ellipse 380px 180px at 420px 820px,var(--glow) 0%,var(--navy) 70%);border:2px solid #000;border-right:1px solid #000;}
  .panel--cover{left:600px;background:var(--navy);border:2px solid #000;border-left:1px solid #000;}
  .photo{position:absolute;border:5px solid var(--frame);box-sizing:border-box;}
  .c{position:absolute;left:0;width:100%;text-align:center;margin:0;}

  .intro-photo{left:58px;top:42px;width:466px;height:232px;background:linear-gradient(120deg,#c8c4c0,#e8dcd0 50%,#b59b86);}
  .family-question{top:286px;font-size:25px;color:var(--white);}
  .family-question .hl{color:var(--yellow);}
  .swab-line{top:366px;font-size:25px;color:var(--white);}
  .swab-line .hl{color:var(--lime);}
  .kids-photo{left:124px;top:412px;width:318px;height:162px;background:linear-gradient(100deg,#5c4030,#8a6a4a 45%,#4d6a35);}
  .impact-note{position:absolute;left:54px;top:588px;width:500px;margin:0;font-family:"Libre Baskerville",serif;font-weight:700;font-size:14.5px;line-height:19.5px;color:var(--yellow);white-space:nowrap;}
  .testing-note{position:absolute;left:20px;top:677px;width:575px;margin:0;font-size:14px;line-height:17px;color:var(--white);white-space:nowrap;}
  .testing-note .lead{font-family:"Libre Baskerville",serif;font-weight:700;font-size:17px;line-height:22px;color:var(--lime);}
  .testing-note .em{font-family:"Libre Baskerville",serif;font-weight:700;font-size:13px;color:var(--lime);}
  .web{font-family:"Arimo",sans-serif;font-size:15px;color:var(--white);}
  .web--inside{position:absolute;left:88px;top:838px;}
  .brand-box{position:absolute;left:429px;top:806px;width:129px;height:87px;background:var(--brand-bg);display:flex;align-items:center;justify-content:center;gap:7px;}
  .brand-box .mark{width:12px;height:12px;border-radius:50%;background:var(--brand-ink);}
  .brand-box .name{font-family:"Crimson Pro",serif;font-weight:600;font-size:17px;color:var(--brand-ink);white-space:nowrap;}

  .tagline{top:26px;font-size:21px;color:var(--yellow);}
  .title{top:58px;font-family:"Russo One",sans-serif;font-size:32px;letter-spacing:1.4px;color:var(--white);white-space:nowrap;}
  .subtitle{top:108px;font-family:"Montserrat",sans-serif;font-weight:600;font-size:17px;letter-spacing:7px;color:var(--white);}
  .tile{position:absolute;width:118px;height:140px;border:3px solid var(--frame);box-sizing:border-box;}
  .question{top:522px;font-family:"Libre Baskerville",serif;font-weight:700;font-size:21px;line-height:28px;color:var(--yellow);}
  .hands-photo{left:96px;top:594px;width:410px;height:232px;background:linear-gradient(90deg,#6f8a3e,#a7b76a 50%,#5d7a3a);}
  .gift{top:836px;font-family:"Libre Baskerville",serif;font-weight:700;font-size:19px;color:var(--lime);}
  .web--cover{top:879px;}
</style>
</head>
<body>
<div class="spread">
  <section class="panel panel--inside">
    <div class="photo intro-photo" role="img" aria-label="Grandparents laughing as a granddaughter kisses her grandfather"></div>
    <p class="c family-question"><span class="hl">DOES CANCER</span> Run in Your Family ?</p>
    <p class="c swab-line">A Simple Swab Could Save A Family Members <span class="hl">LIFE</span></p>
    <div class="photo kids-photo" role="img" aria-label="Grandmother smiling while two grandchildren kiss her cheeks"></div>
    <p class="impact-note">Your decision won’t just affect you. It will also impact<br>Your Family, since your test results may Forecast Their<br>Cancer Risks, too.</p>
    <p class="testing-note"><span class="lead">We believe it is important to understand what can and<br>cannot be learned with genetic testing.</span> Genetic mutations can increase<br>risks for certain cancers, but this does not mean cancer will definitely develop. You should<br>be prepared to receive positive or negative results. &nbsp;&nbsp;&nbsp;<span class="em">Most people receive Negative<br>Results meaning no mutations associated with an increased risk for the<br>Hereditary cancers.</span></p>
    <span class="web web--inside">www.kinshipscreening.com</span>
    <div class="brand-box"><span class="mark"></span><span class="name">Tessaly Labs</span></div>
  </section>

  <section class="panel panel--cover">
    <p class="c tagline">Knowing is better than not knowing. Knowledge is Power !</p>
    <h1 class="c title">HEREDITARY CANCER SCREENING</h1>
    <p class="c subtitle">THE TEST YOU TAKE FOR THEM</p>

    <div class="tile" style="left:48px;top:170px;transform:rotate(-8deg);background:linear-gradient(135deg,#e8e0d8,var(--photo-soft));" role="img" aria-label="Grandmother hugging a young grandchild"></div>
    <div class="tile" style="left:168px;top:166px;transform:rotate(4deg);background:linear-gradient(135deg,#8a6a50,var(--photo-warm));" role="img" aria-label="Smiling grandfather kissed by a grandchild"></div>
    <div class="tile" style="left:290px;top:168px;transform:rotate(-5deg);background:linear-gradient(135deg,#6f9a4a,var(--photo-green));" role="img" aria-label="Multigenerational family sitting on grass"></div>
    <div class="tile" style="left:414px;top:170px;transform:rotate(8deg);background:linear-gradient(135deg,#d6c2ae,#6a4a38);" role="img" aria-label="Grandmother and granddaughter embracing"></div>
    <div class="tile" style="left:46px;top:344px;transform:rotate(10deg);background:linear-gradient(135deg,#b8a090,#5a3e30);" role="img" aria-label="Grandfather with granddaughter cheek to cheek"></div>
    <div class="tile" style="left:170px;top:348px;transform:rotate(-3deg);background:linear-gradient(135deg,#8fb070,#c2b8a8);" role="img" aria-label="Grandfather hugging a small grandson outdoors"></div>
    <div class="tile" style="left:292px;top:346px;transform:rotate(3deg);background:linear-gradient(135deg,#7a9a5a,#c9b098);" role="img" aria-label="Grandparents with grandchildren smiling outdoors"></div>
    <div class="tile" style="left:414px;top:342px;transform:rotate(-8deg);background:linear-gradient(135deg,#dccab8,#a08068);" role="img" aria-label="Grandmother carrying a granddaughter on her back"></div>

    <p class="c question">Will You give Your loved ones the<br>information to Beat Cancer in their lives ?</p>
    <div class="photo hands-photo" role="img" aria-label="A child's hand holding an elder's finger"></div>
    <p class="c gift">Give Them the Gift of Knowledge</p>
    <p class="c web web--cover">www.kinshipscreening.com</p>
  </section>
</div>
</body>
</html>
```